Financial advisory firm needs new business card design

Business card design , simple , elegant, professional. Will use existing logo. One side should be a solid blue background (matching blue in Logo) . info side should have basic info, maybe two color panes. one white, one a different color..maybe light grey. Please visit our website to get feel for colors and business. www.tallowmeadwealth.com

Industry/Entity Type

Financial Service

Contact Information for Business Card

Basic info..minimalist, modern, approach

Colors

Designer to choose colors to be used in the design.

Requirements
Must have
• Important regulatory requirement. The following disclosure MUST be included somewhere on the business card. It can be either front, or back, and it may be in a smaller font (but has to be legible). My interest is to satisfy the requirement with the least possible disruption to the beauty of the card design.
• All securities offered through the Harrowgate Capital, Inc. Oakhurst Lane, NJ. Member QOLTA/DWEM. Advisory services provided through HC Advisory Services, Inc. an PBR Registered Investment Advisor.

```html
<!DOCTYPE html>
<html lang="en">
<head>
<meta charset="utf-8">
<title>Tallowmead Wealth — Business Card</title>
<link href="https://fonts.googleapis.com/css2?family=Open+Sans:wght@400;600;700&display=swap" rel="stylesheet">
<style>
  :root {
    --page: #ececec;
    --card-white: #f7f7f7;
    --card-grey: #6b6c6e;
    --brand-blue: #2b5f98;
    --ink: #3f3f3f;
    --ink-soft: #5a5a5a;
    --rule: #8a8a8a;
    --on-grey: #f2f2f2;
  }
  * { margin: 0; padding: 0; box-sizing: border-box; }
  html, body {
    width: 1200px; height: 872px; overflow: hidden;
    background: var(--page);
    font-family: "Open Sans", sans-serif;
  }
  .stage {
    width: 1200px; height: 872px;
    display: flex; align-items: center; justify-content: center; gap: 40px;
  }
  .card {
    position: relative;
    width: 540px; height: 309px;
    box-shadow: 0 2px 10px rgba(0,0,0,0.10);
  }
  .card--info { background: var(--card-white); color: var(--ink); }
  .card--brand {
    background: var(--card-grey);
    display: flex; align-items: center; justify-content: center;
  }

  .wordmark {
    font-weight: 700; letter-spacing: 0.08em; text-transform: uppercase;
    line-height: 1;
  }
  .card--info .wordmark {
    position: absolute; top: 42px; left: 190px;
    font-size: 26px; color: var(--brand-blue);
  }
  .card--brand .wordmark { font-size: 32px; color: var(--on-grey); }

  .person {
    position: absolute; top: 108px; left: 34px;
  }
  .person__name { font-size: 17px; font-weight: 700; color: var(--brand-blue); }
  .person__title { font-size: 13px; color: var(--ink-soft); margin-bottom: 8px; }
  .company { font-size: 13px; font-weight: 700; color: var(--ink); }
  .address { font-size: 13px; color: var(--ink); line-height: 1.35; }

  .divider {
    position: absolute; top: 150px; left: 300px;
    width: 1px; height: 82px; background: var(--rule);
  }

  .contact {
    position: absolute; top: 150px; left: 318px;
    list-style: none;
  }
  .contact__item {
    display: flex; align-items: center; gap: 9px;
    font-size: 13px; color: var(--ink); height: 27px;
  }
  .contact__item svg { width: 15px; height: 15px; flex: none; }

  .disclosure {
    position: absolute; left: 34px; right: 40px; bottom: 24px;
    font-size: 8.5px; line-height: 1.35; color: var(--ink-soft);
  }
</style>
</head>
<body>
<main class="stage">
  <section class="card card--info" aria-label="Card information side">
    <div class="wordmark">Tallowmead Wealth</div>

    <div class="person">
      <p class="person__name">Elena Marchetti</p>
      <p class="person__title">President &amp; Founder</p>
      <p class="company">Tallowmead Wealth, LLC</p>
      <p class="address">48 Quarry Bend Road, Suite 110<br>Fernhollow, NJ 07145</p>
    </div>

    <div class="divider"></div>

    <ul class="contact">
      <li class="contact__item">
        <svg viewBox="0 0 16 16" aria-hidden="true"><circle cx="8" cy="8" r="7" fill="none" stroke="var(--brand-blue)" stroke-width="1.4"/><path d="M5.6 4.6l1.3 1.6-.7.9c.5 1 1.2 1.7 2.2 2.2l.9-.7 1.6 1.3-.8 1.2c-2.6-.4-4.9-2.7-5.3-5.3z" fill="var(--brand-blue)"/></svg>
        (555) 214-0386
      </li>
      <li class="contact__item">
        <svg viewBox="0 0 16 16" aria-hidden="true"><rect x="1.5" y="3.5" width="13" height="9" fill="var(--brand-blue)"/><path d="M1.5 3.5l6.5 5 6.5-5" fill="none" stroke="var(--card-white)" stroke-width="1.1"/></svg>
        info@tallowmeadwealth.com
      </li>
      <li class="contact__item">
        <svg viewBox="0 0 16 16" aria-hidden="true"><circle cx="8" cy="8" r="7" fill="var(--brand-blue)"/><g fill="none" stroke="var(--card-white)" stroke-width="0.8"><ellipse cx="8" cy="8" rx="3" ry="7"/><path d="M1 8h14M2 4.5h12M2 11.5h12"/></g></svg>
        www.tallowmeadwealth.com
      </li>
    </ul>

    <p class="disclosure">All securities offered through the Harrowgate Capital, Inc. Oakhurst Lane, NJ. Member QOLTA/DWEM. Advisory services provided through HC Advisory Services, Inc. an PBR Registered Investment Advisor.</p>
  </section>

  <section class="card card--brand" aria-label="Card brand side">
    <div class="wordmark">Tallowmead Wealth</div>
  </section>
</main>
</body>
</html>
```